Book cover design : The Hollow Bell

We need a striking book cover design for a book which will be published via Larkspur Reader and as a paperback. The book is a simple short story - ghost story - for children. The book is set in a contemporary English town.

The title of the book is : The Hollow Bell
The author is: Rupert Clowe

The book is a story book, for children, aged approximately 11-15 years old.
It is a ghost story, but not too scary.

Text to go on the front cover:
The Hollow Bell

Rupert Clowe

Text to go on the back cover :

The Hollow Bell; a ghost story of controlled readability for students aged 11 to 15 years, (catch-up reading). Also for students of English as a foreign language.

Target Market(s)

A ghost story of controlled readability for students aged 11 to 15 years, (catch-up reading). Also for students of English as a foreign language.

```html
<!DOCTYPE html>
<html lang="en">
<head>
<meta charset="utf-8">
<title>The Hollow Bell — Rupert Clowe</title>
<link rel="stylesheet" href="https://fonts.googleapis.com/css2?family=Cinzel:wght@400;600&display=swap">
<style>
  :root {
    --backdrop: #e6e7e8;
    --band-blue: #224f71;
    --title-blue: #244f72;
    --paper-white: #f6f8fa;
    --lake-teal: #2f6c7c;
    --mountain-slate: #3e6880;
    --sky-pale: #eaf1f5;
  }
  html, body {
    margin: 0;
    padding: 0;
    width: 1200px;
    height: 1200px;
    overflow: hidden;
    background: var(--backdrop);
  }
  .book-cover {
    position: absolute;
    left: 251px;
    top: 73px;
    width: 698px;
    height: 1053px;
    background: var(--band-blue);
    overflow: hidden;
  }
  .cover-artwork {
    position: absolute;
    left: 0;
    top: 0;
    width: 698px;
    height: 672px;
    background:
      radial-gradient(ellipse 32% 48% at 50% 40%, var(--paper-white) 0%, var(--paper-white) 70%, rgba(246,248,250,0) 100%),
      linear-gradient(to bottom, rgba(246,248,250,0) 55%, var(--paper-white) 82%),
      linear-gradient(to bottom, var(--sky-pale) 0%, var(--mountain-slate) 30%, var(--lake-teal) 52%, #8fb3c0 75%);
  }
  .cover-title {
    position: absolute;
    left: 0;
    top: 0;
    width: 698px;
    height: 800px;
  }
  .cover-title text {
    font-family: 'Cinzel', serif;
    font-weight: 400;
  }
  .title-article { fill: var(--title-blue); }
  .title-main { fill: var(--paper-white); }
  .cover-author {
    position: absolute;
    left: 0;
    width: 698px;
    top: 930px;
    margin: 0;
    text-align: center;
    font-family: 'Cinzel', serif;
    font-weight: 600;
    font-size: 38px;
    letter-spacing: 1px;
    color: var(--paper-white);
  }
</style>
</head>
<body>
  <div class="book-cover">
    <div class="cover-artwork" role="img" aria-label="Double-exposure portrait of a pale woman blended with a misty mountain lake landscape"></div>
    <svg class="cover-title" viewBox="0 0 698 800" aria-label="The Hollow Bell">
      <text class="title-article" x="349" y="664" text-anchor="middle" font-size="168" textLength="290" lengthAdjust="spacingAndGlyphs">THE</text>
      <text class="title-main" x="349" y="782" text-anchor="middle" font-size="124" textLength="688" lengthAdjust="spacingAndGlyphs">HOLLOW BELL</text>
    </svg>
    <p class="cover-author">Rupert Clowe</p>
  </div>
</body>
</html>
```